Marlow Fields Thank-You Tag

Looking for a file that incorporates current branding/colors and says:

"Thanks for Swimming with Us!"
Marlow Fields Otters

Samples of other pieces we've done recently are attached.

Will be printed on cardstock that is
Width: 3.5 inches
Height: 2.5 inches

```html
<!DOCTYPE html>
<html lang="en">
<head>
<meta charset="utf-8">
<title>Marlow Fields Otters – Thank-You Tag</title>
<link rel="stylesheet" href="https://fonts.googleapis.com/css2?family=Bebas+Neue&family=Fira+Sans:wght@700&family=Yellowtail&family=Pacifico&display=block">
<style>
  :root {
    --card-blue: #2c50a3;
    --splash-pink: #f4529b;
    --text-white: #ffffff;
    --mascot-grey: #c4c6cc;
    --page: #ffffff;
  }
  * { margin: 0; padding: 0; box-sizing: border-box; }
  html, body {
    width: 1200px;
    height: 969px;
    overflow: hidden;
    background: var(--page);
  }
  .tag {
    position: absolute;
    left: 142px;
    top: 158px;
    width: 934px;
    height: 667px;
    background: var(--card-blue);
    overflow: hidden;
  }
  .tag-line {
    position: absolute;
    left: 0;
    width: 100%;
    text-align: center;
    white-space: nowrap;
    line-height: 1;
    font-weight: normal;
  }
  .thanks {
    top: 70px;
    font-family: "Yellowtail", "Pacifico", cursive;
    font-size: 82px;
    color: var(--text-white);
  }
  .swimming {
    top: 157px;
    font-family: "Bebas Neue", sans-serif;
    font-size: 120px;
    color: var(--splash-pink);
    letter-spacing: 1px;
  }
  .club-place {
    top: 274px;
    font-family: "Fira Sans", sans-serif;
    font-weight: 700;
    font-size: 47px;
    letter-spacing: 2px;
    color: var(--text-white);
  }
  .club-team {
    top: 312px;
    font-family: "Bebas Neue", sans-serif;
    font-size: 178px;
    letter-spacing: 2px;
    color: var(--splash-pink);
  }
  .mascot {
    position: absolute;
    left: 412px;
    top: 474px;
    width: 108px;
    height: 140px;
    border-radius: 10px;
    background: linear-gradient(180deg, var(--mascot-grey) 0%, var(--mascot-grey) 55%, var(--splash-pink) 100%);
  }
</style>
</head>
<body>
  <main class="tag">
    <p class="tag-line thanks">Thanks for</p>
    <h1 class="tag-line swimming">SWIMMING WITH US!</h1>
    <p class="tag-line club-place">MARLOW FIELDS</p>
    <h2 class="tag-line club-team">OTTERS</h2>
    <div class="mascot" role="img" aria-label="Club mascot illustration leaping above a pink water splash"></div>
  </main>
</body>
</html>
```